Brovan Equipment Sales & Rentals

We are an independent equipment dealership located in the upstate of South Carolina. Our services include Equipment Sales, Equipment Rentals, Metal Sales, and Industrial Supplies.

I have attached our logos and a few billboards that we like as examples for inspiration. Thank you!

Phone Number 864-555-0172

Website link if you want to check out our page.
https://www.brovanmachinery.example

```html
<!DOCTYPE html>
<html lang="en">
<head>
<meta charset="utf-8">
<title>Brovan Equipment Sales &amp; Rentals — Billboard</title>
<link href="https://fonts.googleapis.com/css2?family=Exo+2:ital,wght@0,800;1,800;1,900&display=swap" rel="stylesheet">
<style>
  :root {
    --red-bright: #ff1620;
    --red-deep: #c6000c;
    --red-accent: #ee1c25;
    --ink: #0a0a0a;
    --paper: #ffffff;
    --stage: #ececec;
    --photo-top: #7fa9de;
    --photo-bottom: #a99478;
  }
  * { margin: 0; padding: 0; box-sizing: border-box; }
  html, body { width: 976px; height: 1200px; overflow: hidden; }
  body {
    background: linear-gradient(180deg, #f4f4f4 0%, var(--stage) 100%);
    font-family: "Exo 2", "Arial", sans-serif;
    position: relative;
  }
  .billboard {
    position: absolute;
    left: 28px; top: 370px;
    width: 920px; height: 460px;
    box-shadow: 0 14px 26px rgba(0,0,0,0.35);
  }
  .billboard__art { position: absolute; inset: 0; width: 100%; height: 100%; display: block; }

  .service {
    position: absolute;
    left: 0;
    height: 115px;
    display: flex;
    align-items: center;
    color: var(--paper);
  }
  .service__icon { width: 52px; height: 52px; margin-left: 34px; flex: none; }
  .service__label {
    margin-left: 18px;
    font-style: italic;
    font-weight: 900;
    font-size: 33px;
    line-height: 37px;
    letter-spacing: 0.2px;
  }
  .service--sales   { top: 0; }
  .service--rentals { top: 115px; }
  .service--metal   { top: 230px; }
  .service--supply  { top: 345px; }

  .brand {
    position: absolute;
    left: 295px; top: 345px;
    width: 280px; height: 115px;
    display: flex; align-items: center; justify-content: center;
    gap: 12px;
  }
  .brand__mark { width: 26px; height: 26px; background: var(--red-accent); }
  .brand__name {
    font-weight: 800;
    font-size: 46px;
    color: var(--ink);
    letter-spacing: 1px;
  }

  .contact {
    position: absolute;
    left: 598px; top: 345px;
    width: 312px;
    height: 115px;
    display: flex; flex-direction: column; justify-content: center;
    color: var(--paper);
    font-style: italic;
    font-weight: 900;
  }
  .contact__row { display: flex; align-items: center; gap: 8px; white-space: nowrap; }
  .contact__icon { width: 18px; height: 18px; flex: none; }
  .contact__phone { font-size: 32px; line-height: 38px; letter-spacing: 0.5px; }
  .contact__web { font-size: 16.5px; line-height: 26px; font-weight: 800; }
  .contact__domain { color: var(--red-accent); }
</style>
</head>
<body>
  <section class="billboard" aria-label="Brovan Equipment Sales &amp; Rentals billboard">
    <svg class="billboard__art" viewBox="0 0 920 460" preserveAspectRatio="none">
      <defs>
        <linearGradient id="rowRed" x1="0" y1="0" x2="0" y2="1">
          <stop offset="0" stop-color="var(--red-bright)"/>
          <stop offset="1" stop-color="var(--red-deep)"/>
        </linearGradient>
        <linearGradient id="photoTone" x1="0" y1="0" x2="0" y2="1">
          <stop offset="0" stop-color="var(--photo-top)"/>
          <stop offset="1" stop-color="var(--photo-bottom)"/>
        </linearGradient>
      </defs>
      <polygon points="378,0 920,0 920,345 289,345" fill="url(#photoTone)" role="img" aria-label="Photo of a yellow excavator on a red-earth construction site with a city skyline behind"/>
      <polygon points="0,0 378,0 350,115 0,115" fill="url(#rowRed)"/>
      <polygon points="0,115 350,115 322,230 0,230" fill="url(#rowRed)"/>
      <polygon points="0,230 322,230 289,345 0,345" fill="url(#rowRed)"/>
      <polygon points="0,345 289,345 260,460 0,460" fill="url(#rowRed)"/>
      <polygon points="289,345 590,345 562,460 260,460" fill="var(--paper)"/>
      <polygon points="590,345 920,345 920,460 562,460" fill="var(--ink)"/>
    </svg>

    <div class="service service--sales">
      <svg class="service__icon" viewBox="0 0 50 50" fill="none" stroke="#fff" stroke-width="2.2" stroke-linejoin="round">
        <rect x="8" y="24" width="30" height="12" rx="2"/>
        <rect x="10" y="36" width="30" height="7" rx="3.5"/>
        <path d="M38 28 L46 14 L42 10"/>
        <rect x="14" y="16" width="12" height="8"/>
      </svg>
      <div class="service__label">Equipment<br>Sales</div>
    </div>

    <div class="service service--rentals">
      <svg class="service__icon" viewBox="0 0 50 50" fill="none" stroke="#fff" stroke-width="2.2" stroke-linejoin="round">
        <rect x="12" y="22" width="28" height="12" rx="2"/>
        <rect x="12" y="34" width="30" height="8" rx="4"/>
        <path d="M12 26 L4 12 L10 6 L16 18"/>
        <path d="M4 30 L4 42 L10 42"/>
      </svg>
      <div class="service__label">Equipment<br>Rentals</div>
    </div>

    <div class="service service--metal">
      <svg class="service__icon" viewBox="0 0 50 50" fill="none" stroke="#fff" stroke-width="2.2" stroke-linejoin="round">
        <path d="M8 42 H22 M8 30 H22 M15 30 V42"/>
        <path d="M8 30 L30 8 H44 L22 30 M22 42 L44 20 M37 15 L30 22 M30 22 L30 34"/>
      </svg>
      <div class="service__label">Metal<br>Sales</div>
    </div>

    <div class="service service--supply">
      <svg class="service__icon" viewBox="0 0 50 50" fill="none" stroke="#fff" stroke-width="2.2" stroke-linejoin="round">
        <path d="M4 40 V24 L12 18 V24 L20 18 V24 L28 18 V40 Z"/>
        <rect x="30" y="10" width="6" height="12" rx="3"/>
        <rect x="22" y="34" width="16" height="10"/>
        <path d="M38 37 H44 L47 41 V44 H38"/>
      </svg>
      <div class="service__label">Industrial<br>Supplies</div>
    </div>

    <div class="brand">
      <span class="brand__mark" aria-hidden="true"></span>
      <span class="brand__name">BROVAN</span>
    </div>

    <div class="contact">
      <div class="contact__row contact__phone">
        <svg class="contact__icon" viewBox="0 0 24 24" fill="#fff"><path d="M6.6 10.8a15.1 15.1 0 0 0 6.6 6.6l2.2-2.2a1 1 0 0 1 1-.25 11.4 11.4 0 0 0 3.6.6 1 1 0 0 1 1 1V20a1 1 0 0 1-1 1A17 17 0 0 1 3 4a1 1 0 0 1 1-1h3.5a1 1 0 0 1 1 1c0 1.25.2 2.45.6 3.6a1 1 0 0 1-.25 1z"/></svg>
        <span>864-555-0172</span>
      </div>
      <div class="contact__row contact__web">
        <svg class="contact__icon" viewBox="0 0 24 24" fill="none" stroke="#fff" stroke-width="2"><circle cx="12" cy="12" r="9"/><path d="M3 12h18M12 3c3 3 3 15 0 18M12 3c-3 3-3 15 0 18"/></svg>
        <span>www.<span class="contact__domain">brovanmachinery</span>.example</span>
      </div>
    </div>
  </section>
</body>
</html>
```